New Business Card Design Project

Would like you to take my logo and create a business card much like the Bramblecove leasing.
I can get you the fonts used for the back of the card.
I want the same speckled blue with my logo on it.

Feel free to improve upon the balloon part of the logo if you can.
I put one I was doing with a new balloon and a more "string-like" "I".

```html
<!DOCTYPE html>
<html lang="en">
<head>
<meta charset="utf-8">
<title>Lanternhill Realty — Business Card</title>
<link href="https://fonts.googleapis.com/css2?family=Open+Sans:wght@400;600&display=swap" rel="stylesheet">
<style>
  :root {
    --backdrop: #cfcfcf;
    --backdrop-dark: #b9b9b9;
    --navy: #131a4e;
    --navy-mid: #1d2d78;
    --navy-glow: #2b56a8;
    --white: #ffffff;
    --leaf: #7cbb3c;
    --ink-navy: #1c2a66;
    --decor-light: #f6f8f2;
    --decor-tint: #e4ead9;
  }
  * { box-sizing: border-box; margin: 0; padding: 0; }
  html, body { width: 1200px; height: 900px; overflow: hidden; }
  body {
    background: radial-gradient(ellipse at 50% 40%, var(--backdrop) 0%, var(--backdrop-dark) 100%);
    font-family: "Open Sans", Arial, sans-serif;
    position: relative;
  }
  .card {
    position: absolute;
    top: 300px;
    width: 520px;
    height: 300px;
    border-radius: 28px;
    overflow: hidden;
    box-shadow: 0 14px 28px rgba(0,0,0,0.22);
  }
  .card--back {
    left: 50px;
    background: radial-gradient(ellipse at 48% 45%, var(--navy-glow) 0%, var(--navy-mid) 32%, var(--navy) 72%);
  }
  .card--front { left: 630px; background: var(--white); }

  .wordmark { display: flex; align-items: center; gap: 14px; }
  .wordmark__dot {
    width: 26px; height: 26px; border-radius: 50%;
    background: var(--leaf);
    flex: none;
  }
  .wordmark__name { font-weight: 400; line-height: 1; text-transform: uppercase; }
  .wordmark__name span { display: block; }
  .wordmark__main { font-size: 40px; letter-spacing: 1px; }
  .wordmark__sub { font-size: 22px; letter-spacing: 7px; margin-top: 8px; }

  .card--back .wordmark {
    position: absolute; left: 0; right: 0; top: 100px;
    justify-content: center;
  }
  .card--back .wordmark__name { color: var(--white); }
  .back-url {
    position: absolute; left: 0; right: 0; bottom: 30px;
    text-align: center;
    color: var(--white);
    font-size: 15px;
    letter-spacing: 6.5px;
  }

  .front-top { position: relative; height: 150px; }
  .front-top .wordmark { position: absolute; left: 34px; top: 50px; }
  .front-top .wordmark__name { color: var(--ink-navy); }
  .decor-placeholder {
    position: absolute; right: 0; top: 0;
    width: 90px; height: 150px;
    background: linear-gradient(180deg, var(--decor-light) 0%, var(--decor-tint) 100%);
  }
  .leaf-rule { height: 6px; background: var(--leaf); }
  .front-bottom {
    height: 144px;
    padding: 12px 0 0 30px;
    color: var(--white);
    background: radial-gradient(ellipse at 55% 100%, var(--navy-glow) 0%, var(--navy-mid) 35%, var(--navy) 75%);
  }
  .person__name { color: var(--leaf); font-weight: 600; font-size: 17px; line-height: 20px; }
  .person__role { font-size: 11px; line-height: 14px; margin-bottom: 10px; }
  .contact-list { list-style: none; }
  .contact-list li {
    display: flex; align-items: center; gap: 7px;
    font-size: 13.5px; line-height: 18px;
  }
  .contact-list svg { width: 13px; height: 13px; flex: none; fill: var(--leaf); }
</style>
</head>
<body>

  <section class="card card--back" aria-label="Card back">
    <div class="wordmark">
      <div class="wordmark__dot"></div>
      <div class="wordmark__name">
        <span class="wordmark__main">Lanternhill</span>
        <span class="wordmark__sub">Realty</span>
      </div>
    </div>
    <p class="back-url">www.lanternhillrealty.com</p>
  </section>

  <section class="card card--front" aria-label="Card front">
    <div class="front-top">
      <div class="wordmark">
        <div class="wordmark__dot"></div>
        <div class="wordmark__name">
          <span class="wordmark__main">Lanternhill</span>
          <span class="wordmark__sub">Realty</span>
        </div>
      </div>
      <div class="decor-placeholder" role="img" aria-label="Faint decorative balloons illustration"></div>
    </div>
    <div class="leaf-rule"></div>
    <div class="front-bottom">
      <p class="person__name">Maren Whitlock</p>
      <p class="person__role">Owner/Realtor</p>
      <ul class="contact-list">
        <li>
          <svg viewBox="0 0 16 16" aria-hidden="true"><path d="M3.5 1l2.5 3-1.5 1.8c.8 1.9 2.3 3.4 4.2 4.2L10.5 8.5l3 2.5-1.3 2.8C7 13.6 2.4 9 2.2 3.8z"/></svg>
          555-018-2294
        </li>
        <li>
          <svg viewBox="0 0 16 16" aria-hidden="true"><path d="M8 1a7 7 0 100 14A7 7 0 008 1zm0 1.5c.8 0 1.7 1.6 2 4H6c.3-2.4 1.2-4 2-4zM2.6 6.5h2C4.5 7 4.5 7.5 4.5 8s0 1 .1 1.5h-2a5.6 5.6 0 010-3zm3.4 3h4c-.3 2.4-1.2 4-2 4s-1.7-1.6-2-4zm5.4 0c.1-.5.1-1 .1-1.5s0-1-.1-1.5h2a5.6 5.6 0 010 3z"/></svg>
          www.lanternhillrealty.com
        </li>
        <li>
          <svg viewBox="0 0 16 16" aria-hidden="true"><path d="M1 3h14v10H1zm1.5 1.5v.4L8 9l5.5-4.1v-.4zm0 2.3v4.7h11V6.8L8 10.9z"/></svg>
          marenwhitlock@mail.com
        </li>
        <li>
          <svg viewBox="0 0 16 16" aria-hidden="true"><path d="M8 1.5L1 8h2v6.5h4v-4h2v4h4V8h2z"/></svg>
          218 Harbor Ave., Fairhaven, AL 35000
        </li>
      </ul>
    </div>
  </section>

</body>
</html>
```